varluso.net

We are a IT Service for the valley. I want a clean website, with new Design, like animated pictures. We focus on IT. Give me your best design. What I'm looking for is eye catching. Works with Smart Phones, and Quilo, Tab. Need a section for Submit a support tickets and Remote support. I'm looking for new ideals. I'm open mind, let me see what you guys can do.

Target Market(s)

My clients to see what service and products we have.

Industry/Entity Type

It Service

Requirements
Must have
• Able to submit a trouble tickets and works with Smart Phones, Quilo, Tab.

```html
<!DOCTYPE html>
<html lang="en">
<head>
<meta charset="utf-8">
<title>Varluso – IT Services</title>
<link href="https://fonts.googleapis.com/css2?family=Open+Sans:wght@300;400&family=Roboto+Condensed:wght@400;700&family=Arimo:wght@400;700&display=swap" rel="stylesheet">
<style>
:root{
  --navy:#0b2d55;
  --navy-deep:#06264a;
  --blue:#3f86c2;
  --blue-line:#4a7ab5;
  --brand:#2d3f73;
  --heading-blue:#1b4b9b;
  --panel:#f4f4f4;
  --band:#a9a9a9;
  --text:#333;
  --muted:#8a8a8a;
  --gold:#c08a1a;
  --orange:#d2691e;
  --red:#f4362a;
}
*{margin:0;padding:0;box-sizing:border-box}
html,body{width:1050px;height:1200px;overflow:hidden}
body{position:relative;background:#fff;font-family:"Arimo",Arial,sans-serif;color:var(--text)}
.abs{position:absolute}
.top-strip{left:0;top:0;width:1050px;height:7px;background:var(--blue-line)}
.brand{left:197px;top:44px;display:flex;align-items:center;gap:10px}
.brand-mark{width:13px;height:13px;background:var(--brand)}
.brand-name{font:700 34px/1 "Arimo",Arial,sans-serif;color:var(--brand);letter-spacing:1px}
.util-links{right:330px;top:29px;font-size:9.5px;color:#555;white-space:nowrap}
.util-links span{color:#aaa;margin:0 3px}
.search{left:735px;top:20px;width:151px;height:27px;border:1px solid #3a7bc8;border-radius:3px;background:#fff}
.search-btn{right:-1px;top:-1px;width:34px;height:27px;background:#2f6fb8;border-radius:0 3px 3px 0;display:flex;align-items:center;justify-content:center}
.header-rule{left:165px;top:104px;width:720px;height:1px;background:#c8c8c8}
.contact-icons{left:740px;top:87px;display:flex;gap:8px}
.contact-icons span{width:34px;height:34px;border-radius:50%;border:2px solid #999;background:#fff;display:flex;align-items:center;justify-content:center}
.main-nav{left:0;top:125px;width:1050px;height:35px;background:linear-gradient(100deg,var(--navy-deep) 0%,var(--navy) 20%,#2c5d96 45%,var(--navy) 65%,var(--navy-deep) 100%)}
.main-nav a{position:absolute;top:0;height:35px;font:400 12.5px/35px "Roboto Condensed",sans-serif;color:#fff;text-decoration:none}
.main-nav a.active{left:553px;width:94px;text-align:center;background:#4b7fb5;border:1px solid #c9dcef;color:#1e3550}
.band{left:0;top:160px;width:1050px;height:23px;background:var(--band);border-bottom:2px solid #8e8e8e}
.hero-photo{left:160px;top:183px;width:400px;height:276px;background:linear-gradient(90deg,#e4e6e9 0%,#eef0f2 55%,#fbfbfb 100%)}
.hero-title{left:585px;top:280px;font:300 31px/30px "Open Sans",sans-serif;color:#222;letter-spacing:-1px}
.hero-title .gold{color:var(--gold)}
.hero-title .grey{color:#9a9a9a}
.hero-copy{left:585px;top:383px;width:240px;font:400 10.5px/18px "Open Sans",sans-serif;color:#999}
.hero-more{left:852px;top:313px;font-size:12.5px;color:var(--orange);text-decoration:underline}
.hero-rule{left:0;top:459px;width:1050px;height:4px;background:var(--blue-line)}
.content-bg{left:0;top:463px;width:1050px;height:445px;background:linear-gradient(180deg,#fff 0%,#fff 40%,#cfcfcf 80%,#c4c4c4 100%)}
.content-panel{left:181px;top:470px;width:721px;height:438px;background:var(--panel)}
.welcome{left:199px;top:510px;display:flex;align-items:center;gap:14px;font:700 16.5px "Arimo",sans-serif;color:var(--heading-blue)}
.welcome .brand-name{font-size:18px;color:var(--brand)}
.welcome-copy{left:200px;top:545px;width:397px;font-size:10.6px;line-height:17.2px;text-align:justify;hyphens:auto;-webkit-hyphens:auto;color:#333}
.btn-red{left:475px;top:732px;width:101px;height:32px;border-radius:6px;background:linear-gradient(#ff5a44,var(--red) 55%,#e42418);color:#fff;font-size:12px;line-height:32px;text-align:center}
.news{left:648px;top:473px;width:228px;height:310px;border-radius:10px;background:linear-gradient(160deg,#4c8fcb,#3a7dbd 60%,#3676b6)}
.news h2{position:absolute;left:0;top:16px;width:100%;text-align:center;font:700 20px "Roboto Condensed",sans-serif;color:#fff}
.news hr{position:absolute;left:0;top:55px;width:100%;border:0;height:1px;background:rgba(255,255,255,.35)}
.news-item{position:absolute;left:14px;width:193px;padding-left:20px;font-size:11px;line-height:17px;color:#fff;text-align:justify;hyphens:auto;-webkit-hyphens:auto}
.news-item::before{content:"";position:absolute;left:0;top:3px;width:12px;height:12px;border-radius:50%;background:#8cc4f0}
.clients-rule{left:165px;top:779px;width:475px;height:1px;background:linear-gradient(90deg,transparent,#d2d2d2 20%,#d2d2d2 80%,transparent)}
.clients-title{left:210px;top:802px;font-size:11px;font-weight:700;color:#222}
.ticket{top:842px;width:237px;height:37px;display:flex}
.ticket-icon{width:69px;height:37px;background:linear-gradient(#4a6b85,#284863);display:flex;align-items:center;justify-content:center}
.ticket-label{flex:1;margin-left:1px;background:#b9b8b6;font-size:13.5px;line-height:37px;padding-left:10px;color:#1d3550;white-space:nowrap}
.footer-bg{left:0;top:908px;width:1050px;height:215px;background:var(--blue);border-top:2px solid #8e8e8e}
.footer-panel{left:181px;top:908px;width:721px;height:215px;background:var(--panel)}
.fcol{top:928px;font-size:9.5px;color:var(--muted);line-height:12px}
.fcol h3{font-size:10px;font-weight:700;color:#7b7b7b;margin-bottom:8px}
.fcol ul{list-style:none}
.more li{margin-bottom:7.5px;padding-left:9px;position:relative}
.more li::before{content:"•";position:absolute;left:0}
.connect li{display:flex;gap:5px;margin-bottom:7.5px}
.connect i{flex:none;width:11px;height:11px;display:block}
.follow{display:flex;gap:4px;align-items:center;margin:4px 0 9px}
.follow b{border:1px solid #9aa;border-radius:2px;padding:1px 3px;font-weight:400;color:#235;background:#fff}
.follow em{font-style:normal;border:1px solid #bcd;border-radius:2px;padding:1px 4px;color:#235;background:#fff}
.phone-img{left:551px;top:1008px;width:26px;height:49px;border-radius:4px;background:linear-gradient(#444,#666 50%,#444)}
.badge{left:727px;top:928px;width:73px;height:29px;border:1px solid #b0b0b0;background:#eaeaea}
.copyright{left:0;top:1123px;width:1050px;height:77px;background:var(--navy-deep);text-align:center;font-size:10.5px;line-height:86px;color:#b7c2cf}
</style>
</head>
<body>
<div class="abs top-strip"></div>

<header>
  <div class="abs brand"><span class="brand-mark"></span><span class="brand-name">VARLUSO</span></div>
  <div class="abs util-links">LOGIN<span>|</span>Blog<span>|</span>News<span>|</span>Partners</div>
  <div class="abs search">
    <div class="abs search-btn">
      <svg width="18" height="18" viewBox="0 0 18 18"><circle cx="7.5" cy="7.5" r="5.5" fill="none" stroke="#fff" stroke-width="2.2"/><line x1="11.5" y1="11.5" x2="16.5" y2="16.5" stroke="#fff" stroke-width="2.6" stroke-linecap="round"/></svg>
    </div>
  </div>
  <div class="abs header-rule"></div>
  <div class="abs contact-icons">
    <span><svg width="20" height="16" viewBox="0 0 20 16"><path d="M2 5c0-3 16-3 16 0v2h-4V5H6v2H2z" fill="#555"/><rect x="5" y="8" width="10" height="7" rx="1" fill="#555"/></svg></span>
    <span><svg width="20" height="14" viewBox="0 0 20 14"><rect x="1" y="1" width="18" height="12" rx="2" fill="#555"/><path d="M1 2l9 6 9-6" fill="none" stroke="#fff" stroke-width="1.3"/></svg></span>
    <span><svg width="20" height="18" viewBox="0 0 20 18"><rect x="1" y="1" width="12" height="8" rx="2" fill="#555"/><rect x="7" y="6" width="12" height="8" rx="2" fill="#777"/><path d="M14 14l2 3v-3z" fill="#777"/></svg></span>
  </div>
</header>

<nav class="abs main-nav">
  <a style="left:481px">COMPANY</a>
  <a class="active">SERVICES</a>
  <a style="left:658px">CAREER</a>
  <a style="left:731px">SAPPORT</a>
  <a style="left:814px">CONTACT</a>
</nav>
<div class="abs band"></div>

<section class="hero">
  <div class="abs hero-photo" role="img" aria-label="Photo of support agents wearing headsets"></div>
  <h1 class="abs hero-title">The Best<br><span class="gold">You Can Find</span><br><span class="grey">On The Web</span></h1>
  <p class="abs hero-copy">Tessaro is a leading provider of BPO services focusing on multiple horizontals and verticals.</p>
  <a class="abs hero-more">Read More</a>
</section>
<div class="abs hero-rule"></div>

<main>
  <div class="abs content-bg"></div>
  <div class="abs content-panel"></div>
  <h2 class="abs welcome">WELCOME TO <span class="brand-name">VARLUSO</span></h2>
  <p class="abs welcome-copy">Tessaro Informatic System provide a broad portfolio of information technology solution to our clients worldwide.<br>Our consultants know exactly what to do to improve your business process and requirements of IT solutions to your business. Regardless of industry, we offer flexible &amp; suitable solutions.<br>Tessaro Informatic System provide a broad portfolio of information technology solution to our clients worldwide.<br>Our consultants know exactly what to do to improve your business process and requirements of IT solutions to your business. Regardless of industry, we offer flexible &amp; suitable solutions.</p>
  <a class="abs btn-red">Read More</a>

  <aside class="abs news">
    <h2>News and Events</h2>
    <hr>
    <p class="news-item" style="top:85px">Tessaro Informatic System provide a broad portfolio ur clients worldwide.</p>
    <p class="news-item" style="top:163px">Tessaro Informatic System provide a broad portfolio ur clients worldwide.</p>
    <p class="news-item" style="top:236px">Tessaro Informatic System provide a broad portfolio ur clients worldwide.</p>
  </aside>

  <div class="abs clients-rule"></div>
  <h3 class="abs clients-title">Our Clients</h3>
  <a class="abs ticket" style="left:210px">
    <span class="ticket-icon"><svg width="28" height="22" viewBox="0 0 28 22"><rect x="1" y="6" width="26" height="15" fill="none" stroke="#fff" stroke-width="1.6"/><path d="M1 6l13 9 13-9M6 6V1h16v5" fill="none" stroke="#fff" stroke-width="1.6"/></svg></span>
    <span class="ticket-label">Submit a support tickets</span>
  </a>
  <a class="abs ticket" style="left:636px">
    <span class="ticket-icon"><svg width="26" height="22" viewBox="0 0 26 22"><rect x="1" y="1" width="24" height="15" rx="1" fill="none" stroke="#fff" stroke-width="1.8"/><path d="M10 16v4h6v-4M7 21h12" stroke="#fff" stroke-width="1.8" fill="none"/></svg></span>
    <span class="ticket-label">Submit a support tickets</span>
  </a>
</main>

<footer>
  <div class="abs footer-bg"></div>
  <div class="abs footer-panel"></div>
  <div class="abs fcol more" style="left:196px">
    <h3>More details</h3>
    <ul><li>Privacy Statement</li><li>Legal</li><li>Useful Links</li><li>Contact Us</li><li>Sitemap</li></ul>
  </div>
  <div class="abs fcol connect" style="left:373px;width:155px">
    <h3>Connect with us</h3>
    <ul>
      <li><i style="background:#7fb0d8"></i>Subscribe to our newsletter</li>
      <li><i style="background:#f08a24"></i>RSS</li>
      <li><i style="background:#5fb6e6"></i>Chirpa</li>
      <li><i style="background:#2a6aa5"></i>Linkora - Orvane Agency Company Profile</li>
    </ul>
    <div class="follow"><i style="width:13px;height:13px;display:block;background:#2a6aa5"></i><b>Follow</b><em>6,413</em></div>
    <ul>
      <li><i style="background:#2a6aa5"></i>Linkora - Innovate Orvane</li>
      <li><i style="background:#e33"></i>Vidora</li>
    </ul>
  </div>
  <div class="abs fcol" style="left:550px;width:150px">
    <h3 style="margin-bottom:5px">Connect &amp; Invest in Orvane</h3>
    <p>Orvane has recently launched a new blogging platform.</p>
    <h3 style="margin:18px 0 8px">Orvane mobile</h3>
    <p style="padding-left:37px;font-size:9px">Orvane has recently launched an optimised version of our website for Mobile.</p>
  </div>
  <div class="abs phone-img" role="img" aria-label="Mobile phone showing the mobile website"></div>
  <div class="abs badge" role="img" aria-label="Funding programme badge"></div>
  <p class="abs fcol" style="left:727px;top:966px;width:156px;font-size:8.5px;color:#666">Funded by the Regional Council under the Regional Growth Plan 2007-2013</p>
  <div class="abs copyright">© 2010-2013 Tessaro Informatic System. All Rights Reserved</div>
</footer>
</body>
</html>
```